Square graphic for social media post

I want to create a 1080 x 1080px all-black image for the quote below that I can share on social media. I want the emphasis to be primarily on the quote, secondarily on the portrait, and third (smallest) on the logo. I want the background on the portrait to be edited so it's transparent and just shows the face of the person on a black background (no brick wall visible).

Graphic color: black
Text color: white
Content: "What we went through is going to make the greatest generation of hoteliers our industry has ever seen." << biggest text
Dorian Welk << smaller text
President, Marrowgate Hotels << smaller text
[image of person - use whichever version looks better to you]
[Add Lodging Ledger logo - whichever looks better to you]

This image needs to be readable when sized down much smaller (400x400?) so want the text and portrait to take up most of the space.

I'd like the output both as PNG and original file (preferably Canva). Thanks!

Target Market(s)

Hotel managers

Industry/Entity Type

Hospitality

Font styles to use
Sans Serif

Colors

Designer to choose colors to be used in the design.

Requirements
Must have
• Needs to focus on the quote and the person quoted (the portrait)

```html
<!DOCTYPE html>
<html lang="en">
<head>
<meta charset="utf-8">
<title>Quote card – Dorian Welk</title>
<link rel="stylesheet" href="https://fonts.googleapis.com/css2?family=Montserrat:wght@400;500&display=swap">
<style>
  :root {
    --bg: #000000;
    --panel: #0e0e0e;
    --ink: #ffffff;
    --portrait-light: #d9d9d9;
    --portrait-mid: #8a8f99;
    --portrait-dark: #2f4f8a;
  }
  * { margin: 0; padding: 0; box-sizing: border-box; }
  html, body {
    width: 1200px;
    height: 1200px;
    overflow: hidden;
    background: var(--bg);
  }
  .card {
    position: relative;
    width: 1200px;
    height: 1200px;
    background: var(--bg);
    color: var(--ink);
    font-family: "Montserrat", sans-serif;
  }
  .brand-panel {
    position: absolute;
    top: 0;
    left: 0;
    width: 348px;
    height: 228px;
    background: var(--panel);
    display: flex;
    align-items: center;
    justify-content: center;
  }
  .brand-name {
    font-size: 21px;
    font-weight: 500;
    letter-spacing: 4px;
    text-transform: uppercase;
    color: var(--ink);
  }
  .corner-panel {
    position: absolute;
    top: 0;
    right: 0;
    width: 214px;
    height: 217px;
    background: var(--panel);
  }
  .portrait {
    position: absolute;
    top: 72px;
    left: 397px;
    width: 406px;
    height: 468px;
    background:
      linear-gradient(180deg, transparent 55%, var(--portrait-dark) 100%),
      linear-gradient(135deg, var(--portrait-light) 0%, var(--portrait-mid) 100%);
  }
  .quote {
    position: absolute;
    top: 603px;
    left: 0;
    width: 1200px;
    text-align: center;
    font-size: 56px;
    font-weight: 400;
    line-height: 80px;
    letter-spacing: 0.3px;
  }
  .attribution {
    position: absolute;
    top: 993px;
    left: 0;
    width: 1200px;
    text-align: center;
  }
  .attribution-name {
    font-size: 29px;
    font-weight: 400;
    line-height: 40px;
  }
  .attribution-role {
    font-size: 25px;
    font-weight: 400;
    line-height: 40px;
    margin-top: 6px;
  }
  .rule {
    position: absolute;
    top: 1117px;
    left: 120px;
    width: 960px;
    height: 5px;
    border-radius: 3px;
    background: var(--ink);
  }
</style>
</head>
<body>
  <main class="card">
    <div class="brand-panel">
      <span class="brand-name">Lodging Ledger</span>
    </div>
    <div class="corner-panel"></div>

    <div class="portrait" role="img" aria-label="Portrait of Dorian Welk, smiling, in a blue blazer and white shirt"></div>

    <blockquote class="quote">
      "What we went through is<br>
      going to make the greatest<br>
      generation of hoteliers our<br>
      industry has ever seen."
    </blockquote>

    <div class="attribution">
      <p class="attribution-name">Dorian Welk</p>
      <p class="attribution-role">President, Marrowgate Hotels</p>
    </div>

    <div class="rule"></div>
  </main>
</body>
</html>
```